Boutique High End Custom Furniture Store, Client Appreciation Card

We are looking to create a 5 x 7 card for our best clients that offer a 15% discount on their next furniture purchase. We would like to use both sides, full colour.

We are a high-end boutique furniture store located in Calgary, AB, Canada.

I have attached a card we did for our grand reopening that we like -- it's fresh with lots of white space. I have attached the image we used as well as a possible second image of furniture.

I have also attached other examples -- all seem fresh and clean with a layer of luxury.

I have attached all versions of our logo in an EPS file.

Target Market(s)

High disposable income, women over 40 who love style, contemporary design and fine art. Think Lila Morrow, Finn Ashby, Rue Dalston perfume and http://www.marlowquinby.example/

Industry/Entity Type

Boutique

Font styles to use
Sans Serif
Script

Colors
33a6d7
0592cd
85cae6
eda3c7
e667a6

Requirements
Must have
• Must be colour on both side (one side logo perhaps), the other side has content? Card needs to be 5 x 7 (either orientation is okay). Card needs to be fresh, stylish and current with the use of colour i.e. not all black and white. Logo needs to be prominent on either side.
• Please also have a look at our website.
Should not have
• Should not feel traditional or dated but at the same time not too playful so that it looks unprofessional. We are not "Gil's bargain Couches"!

```html
<!DOCTYPE html>
<html lang="en">
<head>
<meta charset="utf-8">
<title>Alcove Atelier – Client Appreciation Card</title>
<link href="https://fonts.googleapis.com/css2?family=Lato:wght@300;400;700&family=Dancing+Script:wght@600&display=swap" rel="stylesheet">
<style>
:root{
  --teal:#4fb2b6;
  --teal-dark:#3a9ea3;
  --teal-light:#8fd0d2;
  --ink:#2b2b2b;
  --grey:#555;
  --rule:#9a9a9a;
  --paper:#ffffff;
  --backdrop:#e9e9e9;
  --photo-a:#f3f4f4;
  --photo-b:#dfe2e2;
  --photo-warm:#cfc9c2;
}
*{box-sizing:border-box;margin:0;padding:0}
html,body{width:1200px;height:960px;overflow:hidden;background:var(--backdrop);font-family:'Lato',sans-serif;color:var(--ink)}
.card{position:absolute;left:285px;width:630px;height:450px;background:var(--paper);box-shadow:0 4px 16px rgba(0,0,0,.12);overflow:hidden}
.card--front{top:20px}
.card--back{top:490px}
.card svg.shapes{position:absolute;inset:0}
.abs{position:absolute}

.brand{text-align:center}
.brand__name{font-weight:400;font-size:28px;letter-spacing:.5px;color:var(--ink);display:inline-flex;align-items:center;gap:10px}
.brand__mark{width:10px;height:10px;border-radius:50%;background:var(--teal)}
.brand__tag{font-weight:300;font-size:13px;font-style:normal;color:var(--grey);margin-top:2px}

.front-copy{left:385px;width:230px;top:34px;text-align:center}
.gift{display:flex;align-items:center;gap:8px;margin-top:40px;font-weight:300;font-size:15px;letter-spacing:.5px;color:var(--grey)}
.gift::before,.gift::after{content:"";flex:1;height:1px;background:var(--grey)}
.offer{font-weight:300;font-size:34px;color:var(--teal-dark);margin-top:16px;white-space:nowrap}
.offer-sub{font-weight:400;font-size:14px;color:var(--teal-dark);margin-top:4px;text-transform:uppercase}
.terms{font-weight:400;font-size:12px;line-height:1.45;color:var(--grey);margin-top:18px}
.divider-dot{width:11px;height:11px;border:2px solid var(--teal);margin:24px auto 0;transform:rotate(45deg)}
.contact{font-size:12.5px;line-height:1.5;color:var(--ink);margin-top:24px;white-space:nowrap}

.badge{border-radius:50%;background:var(--teal);border:4px solid var(--paper);box-shadow:0 0 0 2px var(--teal-light);color:var(--paper);display:flex;flex-direction:column;align-items:center;justify-content:center;text-align:center}
.badge--script{left:272px;top:292px;width:108px;height:108px;font-family:'Dancing Script',cursive;font-size:21px;line-height:1.05}
.badge--offer{left:440px;top:190px;width:112px;height:112px;font-size:9.5px;text-transform:uppercase;letter-spacing:.5px}
.badge--offer strong{font-size:24px;font-weight:700;text-transform:none;letter-spacing:0;line-height:1.1}

.back-brand{left:380px;top:22px;text-align:left}
.back-brand .brand__name{font-size:19px}
.back-brand .brand__tag{font-size:10px;padding-left:20px}
.address-lines{left:405px;top:82px;width:200px}
.address-lines span{display:block;height:1px;background:var(--rule);margin-bottom:30px}

.about{left:30px;top:302px;width:380px;text-align:center;color:var(--teal-dark);font-size:13.5px;line-height:1.4}
.about-rule{height:1px;background:var(--teal);margin:10px 0}
.about-contact{color:var(--ink);font-size:12.5px;line-height:1.45}
</style>
</head>
<body>

<section class="card card--front" aria-label="Card front">
  <svg class="shapes" width="630" height="450" viewBox="0 0 630 450">
    <defs>
      <linearGradient id="roomFront" x1="0" y1="0" x2="0" y2="1">
        <stop offset="0" stop-color="var(--photo-a)"/>
        <stop offset="1" stop-color="var(--photo-b)"/>
      </linearGradient>
    </defs>
    <path role="img" aria-label="Photo of a styled entry with round mirror, black side table, vase of teal eucalyptus and a turquoise upholstered bench" d="M0 0 H318 C298 110 350 200 338 300 C330 370 310 420 282 450 H0 Z" fill="url(#roomFront)"/>
    <path d="M318 0 C298 110 350 200 338 300 C330 370 310 420 282 450" fill="none" stroke="var(--teal)" stroke-width="12"/>
    <path d="M336 0 C316 110 368 200 356 300 C348 370 328 420 300 450" fill="none" stroke="var(--teal-light)" stroke-width="3"/>
  </svg>

  <div class="abs front-copy">
    <div class="brand">
      <div class="brand__name"><span class="brand__mark"></span>Alcove Atelier</div>
      <div class="brand__tag">Curated homes, Calgary</div>
    </div>
    <div class="gift">OUR GIFT TO YOU</div>
    <div class="offer">Enjoy 15% off</div>
    <div class="offer-sub">at Alcove Atelier</div>
    <p class="terms">Offer is good for one-time use and cannot be combined with other offers.</p>
    <div class="divider-dot"></div>
    <p class="contact">403.555.0182<br>hello@alcove.example | alcove.example<br>2210 Linden Ave SW, Calgary AB</p>
  </div>

  <div class="abs badge badge--script">love<br>where you<br>live</div>
</section>

<section class="card card--back" aria-label="Card back">
  <svg class="shapes" width="630" height="450" viewBox="0 0 630 450">
    <defs>
      <linearGradient id="roomBack" x1="0" y1="0" x2="1" y2="1">
        <stop offset="0" stop-color="var(--photo-a)"/>
        <stop offset="1" stop-color="var(--photo-warm)"/>
      </linearGradient>
    </defs>
    <path role="img" aria-label="Photo of a taupe sideboard with framed artwork, a small tower sculpture and a yellow vase of white flowers" d="M0 0 H292 C335 80 375 150 392 232 C300 270 150 282 0 290 Z" fill="url(#roomBack)"/>
    <path d="M300 0 C350 90 430 170 445 260 C455 330 470 400 480 450" fill="none" stroke="var(--teal)" stroke-width="12"/>
    <path d="M322 0 C372 90 452 170 467 260 C477 330 492 400 502 450" fill="none" stroke="var(--teal-light)" stroke-width="3"/>
  </svg>

  <div class="abs brand back-brand">
    <div class="brand__name"><span class="brand__mark"></span>Alcove Atelier</div>
    <div class="brand__tag">Curated homes, Calgary</div>
  </div>

  <div class="abs address-lines"><span></span><span></span><span></span></div>

  <div class="abs badge badge--offer">Enjoy<strong>15% off</strong>Alcove Atelier</div>

  <div class="abs about">
    <p>Alcove Atelier is a unique boutique custom furniture store offering a wide selection of furniture, rugs, bedding, lighting, window coverings, accessories and interior design services.</p>
    <div class="about-rule"></div>
    <p class="about-contact">403.555.0182 hello@alcove.example | alcove.example<br>2210 Linden Ave SW, Calgary AB</p>
  </div>
</section>

</body>
</html>
```